Brighten Every Calling book cover and updated company logo bundle

USE THE LOGO ON THE BACK COVER. I WANT AN UPDATED LOOK TO MY LOGO
Size of book: 5.5 x 8.5
Title: Brighten Every Calling
Subtitle: An introvert’s guide to creating a coaching business that reflects who you are
The Subtitle does NOT go on the book cover
Author: Marla Toppington
BOOK DESCRIPTION: This book will help coaches and creative professionals get confidently clear on who they are so they can create a business that reflects their inner message.

DEMOGRAPHICS — Coaches and creative professional age 35-45

WOULD YOU PREFER PEOPLE OR OBJECTS ON YOUR COVER?
Objects or abstract designs
Anything I don’t want on the cover? people
Objects or symbols I want on the cover: possibly magnifying glass

IF YOU HAVE ANY PHOTOS THAT YOU WOULD LIKE US TO USE, PLEASE INCLUDE THE LINK(S) HERE. My logo or face pic for the back cover (Face pic pending)

COPY FOR THE SPINE
Brighten Every Calling
Marla Toppington
Lanternhall Books (with logo)

COPY FOR THE BACK COVER (270 words) my biz logo at the bottom and my picture next to my short bio. (Picture to come)

Create a Coaching Business that Reflects Who You Are

Do you want to step confidently into your new career by doing what you love? You aren't alone! But instead of doing what they love, many new coaches get stuck by trying to fit into traditional ways of doing business and create many unnecessary hurdles to happiness and success.
In this book, creative business coach, Marla Toppington teaches you, as she has taught herself and many others, to stop feeling guilty about what you “should” do in your life and in the process you will learn how to turn your passion into a purposeful career.

New coaches will learn how to:
• Recognize how your life decisions to this point are holding you back.
• Discover your gifts so you can express yourself through your creative projects.
• Identify and develop tools to bring your passion into purpose
• Offer services based on what you love to do.
• Understand your personal work style and work-flow to optimize your ideas and productivity.
• Create a message that reflects who you are to attract clients to work with you.
• Ask confidently for what you are worth and get it every time.
Join Marla on the journey of reconnecting with yourself and manifesting your dream.

Marla Toppington, founder of Quiet Harbor Wellness, helps new coaches and creative entrepreneurs find their inner voice so that they have the confidence to bring their authentic selves out into the world. Marla has gone through this process for herself and helped other new businesses achieve dramatic improvements in their organization and focus as a result.

Target Market(s)

indicated in description

Industry/Entity Type

Life Coaching

Logo Text

Quiet Harbor Wellness

Requirements
Must have
• updated look on existing logo it is going on the back of the book
Nice to have
• I like the font in the book cover I attached but Id like to see what else is possible

```html
<!DOCTYPE html>
<html lang="en">
<head>
<meta charset="utf-8">
<title>Brighten Every Calling – Book Cover</title>
<link href="https://fonts.googleapis.com/css2?family=Cinzel+Decorative:wght@400;700&family=Marcellus&family=Open+Sans:wght@400;600&display=swap" rel="stylesheet">
<style>
  :root {
    --mint-light: #c9ecd6;
    --mint: #9fd6bd;
    --teal: #6fb5a5;
    --teal-deep: #4f9488;
    --violet: #6a2fb0;
    --violet-deep: #4b1d86;
    --ink: #1c1c1c;
    --paper: #ffffff;
    --glass: #d7eee2;
    --ivory: #ead9a2;
  }
  html, body {
    margin: 0;
    padding: 0;
    overflow: hidden;
    background: #ffffff;
  }
  .cover {
    position: relative;
    width: 1200px;
    height: 882px;
    overflow: hidden;
    font-family: "Open Sans", Arial, sans-serif;
    color: var(--ink);
    background:
      radial-gradient(ellipse 520px 420px at 180px 160px, rgba(232,250,238,0.85), transparent 70%),
      radial-gradient(ellipse 480px 520px at 1050px 700px, rgba(80,150,135,0.45), transparent 70%),
      radial-gradient(ellipse 420px 360px at 760px 260px, rgba(170,220,200,0.55), transparent 70%),
      linear-gradient(115deg, var(--mint-light) 0%, var(--mint) 40%, var(--teal) 75%, var(--teal-deep) 100%);
  }

  /* ---------- back cover ---------- */
  .back {
    position: absolute;
    left: 25px;
    top: 33px;
    width: 518px;
  }
  .back-heading {
    margin: 0 0 12px;
    font-weight: 400;
    font-size: 19px;
    color: var(--violet);
  }
  .back-copy {
    margin: 0;
    font-size: 14.6px;
    line-height: 1.3;
  }
  .learn-heading {
    margin: 34px 0 4px;
    text-align: center;
    font-weight: 600;
    font-size: 17.5px;
  }
  .learn-list {
    margin: 0;
    padding: 0;
    width: 478px;
    list-style: none;
    font-size: 14.6px;
    line-height: 19.4px;
  }
  .learn-list li {
    padding-left: 26px;
    text-indent: -10px;
  }
  .learn-list li::before {
    content: "• ";
  }
  .closing {
    margin: 18px 0 0;
    font-size: 14.6px;
    line-height: 1.3;
    text-align: justify;
  }
  .author-photo {
    position: absolute;
    left: 25px;
    top: 556px;
    width: 125px;
    height: 159px;
    background: var(--paper);
  }
  .bio {
    position: absolute;
    left: 184px;
    top: 566px;
    width: 357px;
    margin: 0;
    font-size: 13.6px;
    line-height: 18.6px;
    text-align: justify;
  }

  /* ---------- bottom band ---------- */
  .imprint-band {
    position: absolute;
    left: 0;
    top: 814px;
    width: 629px;
    height: 39px;
    background: var(--paper);
  }
  .brand {
    position: absolute;
    left: 44px;
    top: 11px;
    display: flex;
    align-items: center;
    gap: 6px;
    font-size: 12px;
    font-weight: 600;
    color: var(--violet-deep);
  }
  .brand-dot {
    width: 14px;
    height: 14px;
    border-radius: 50%;
    background: #f08a1c;
  }
  .publisher {
    position: absolute;
    left: 560px;
    top: 7px;
    width: 64px;
    text-align: center;
    font-size: 9px;
    line-height: 1.2;
    font-weight: 600;
    color: var(--ink);
  }

  /* ---------- spine ---------- */
  .spine-title,
  .spine-author {
    position: absolute;
    left: 597px;
    transform-origin: 0 0;
    transform: rotate(90deg);
    white-space: nowrap;
  }
  .spine-title {
    top: 84px;
    margin-left: 16px;
    font-family: "Cinzel Decorative", Georgia, serif;
    font-size: 29px;
    color: var(--violet);
    letter-spacing: 0.5px;
  }
  .spine-author {
    top: 604px;
    margin-left: 13px;
    font-family: "Marcellus", Georgia, serif;
    font-size: 23px;
    color: var(--paper);
  }

  /* ---------- front cover ---------- */
  .front-art {
    position: absolute;
    left: 790px;
    top: 226px;
    width: 246px;
    height: 530px;
    border-radius: 123px 123px 24px 24px;
    background: linear-gradient(180deg, var(--glass) 0%, var(--glass) 44%, var(--ivory) 56%, var(--ivory) 100%);
    opacity: 0.55;
  }
  .front-title {
    position: absolute;
    left: 640px;
    top: 18px;
    width: 555px;
    margin: 0;
    text-align: center;
    font-family: "Cinzel Decorative", Georgia, serif;
    font-weight: 400;
    font-size: 84px;
    line-height: 128px;
    color: var(--violet);
    text-shadow: 2px 3px 4px rgba(40,20,70,0.35);
  }
  .front-title span {
    display: block;
  }
  .front-author {
    position: absolute;
    left: 640px;
    top: 822px;
    width: 555px;
    margin: 0;
    text-align: center;
    font-family: "Marcellus", Georgia, serif;
    font-weight: 400;
    font-size: 34px;
    color: var(--paper);
  }
</style>
</head>
<body>
<main class="cover">

  <section class="back">
    <h2 class="back-heading">Create a Coaching Business that Reflects Who You Are</h2>
    <p class="back-copy">Do you want to step confidently into your new career by doing what you love? You aren't alone! But instead of doing what they love, many new coaches get stuck by trying to fit into traditional ways of doing business and create many unnecessary hurdles to happiness and success.<br>In this book, creative business coach, Marla Toppington teaches you, as she has taught herself and many others, to stop feeling guilty about what you “should” do in your life and in the process you will learn how to turn your passion into a purposeful career.</p>
    <h3 class="learn-heading">New coaches will learn how to:</h3>
    <ul class="learn-list">
      <li>Recognize how your life decisions to this point are holding you back.</li>
      <li>Discover your gifts so you can express yourself through your creative projects.</li>
      <li>Identify and develop tools to bring your passion into purpose</li>
      <li>Offer services based on what you love to do.</li>
      <li>Understand your personal work style and work-flow to optimize your ideas and productivity.</li>
      <li>Create a message that reflects who you are to attract clients to work with you.</li>
      <li>Ask confidently for what you are worth and get it every time.</li>
    </ul>
    <p class="closing">Join Marla on the journey of reconnecting with yourself and manifesting your dream.</p>
  </section>

  <div class="author-photo" role="img" aria-label="Author portrait placeholder"></div>
  <p class="bio"><strong>Marla Toppington</strong>, founder of Quiet Harbor Wellness, helps new coaches and creative entrepreneurs find their inner voice so that they have the confidence to bring their authentic selves out into the world. Marla has gone through this process for herself and helped other new businesses achieve dramatic improvements in their organization and focus as a result.</p>

  <div class="imprint-band">
    <div class="brand"><span class="brand-dot"></span>Quiet Harbor Wellness</div>
    <div class="publisher">Lanternhall<br>Books</div>
  </div>

  <div class="spine-title">Brighten Every Calling</div>
  <div class="spine-author">Marla Toppington</div>

  <div class="front-art" role="img" aria-label="Photograph of an upright magnifying glass with an ivory handle, its lens over the title"></div>
  <h1 class="front-title"><span>Brighten</span><span>Every</span><span>Calling</span></h1>
  <p class="front-author">Marla Toppington</p>

</main>
</body>
</html>
```